New Website for consulting company

We need a completely new design for our company web site: www.morvane-partners.ch (please do not use it as a reference. We want something completely different.)
We are a consulting company and therefore our team is our key ressource together with our skills.
This site will be german in the first place. It will be the webmasters job to create it multilingual.
The website should be rather eccentric but still informative.
For colors and logo please refer to attached Logodefinition.pdf. The colored horizontal logo should be somehow used for the website but doesn't need to be extremely prominent. You can choose every color for the design but the logo must be somehow embedded in original colors and the green should be integrated for the site.
Please keep in mind that it should also work for mobile devices so the webmaster will have to create a responsive website out of the submitted design.
The main Page should be a one pager with different layout blocks directly accessible via top sticky menubar.:
- AKTEURE (team), gallery, people centric with images of member and expandable description box, plus skills abstract list (name & description). See attached mockups to support the explaining (do not take it as a reference).
- ÜBER UNS (mission), Description of companies vision, mission, competences etc.
- ... according to the menu bar
We would like to have at least 3 different block layouts to fill with content for the one pager site:
1. Team is the most important and the least generic one
2. Big picture less text
3. Multiple smaller pictures multiple text blocks
4. Hardly any picture text centric
The page should communicate competence in what we are doing, quality and not least youth and freshness.
See Attachements:
- Logodefinition.pdf: Logo definition containing definition of color of the logo.
- mockup_Website_mock1.png: These should give you an impression of how it is meant to have layouted blocks

```html
<!DOCTYPE html>
<html lang="en">
<head>
<meta charset="utf-8">
<title>Morvane Partners – Team</title>
<link rel="stylesheet" href="https://fonts.googleapis.com/css2?family=Lato:wght@300;400;700;900&display=swap">
<style>
  :root {
    --green: #6cc04a;
    --green-dark: #58a83a;
    --ink: #3a3a3a;
    --text: #8a8a8a;
    --paper: #ffffff;
    --panel: #f4f4f4;
    --stage: #e6e7e5;
    --line: #e2e2e2;
    --suit: #2c3545;
    --shirt: #9cb9d8;
  }
  * { box-sizing: border-box; margin: 0; padding: 0; }
  html, body { width: 1200px; height: 800px; overflow: hidden; }
  body {
    background: var(--stage);
    font-family: "Lato", Arial, sans-serif;
    color: var(--ink);
    position: relative;
  }

  /* ---------- desktop page ---------- */
  .desktop-page {
    position: absolute; left: 30px; top: 40px;
    width: 790px; height: 720px;
    background: var(--paper);
    overflow: hidden;
  }
  .team-row {
    display: flex; gap: 20px;
    padding: 0 40px;
    height: 230px;
  }
  .member-card { position: relative; flex: 1; }
  .member-photo {
    height: 180px;
    background: linear-gradient(180deg, var(--suit) 0%, #3d4a60 55%, var(--shirt) 100%);
  }
  .member-card:nth-child(2) .member-photo {
    background: linear-gradient(180deg, var(--shirt) 0%, #b9cfe6 60%, var(--suit) 100%);
  }
  .name-tag {
    position: absolute; left: -6px; top: 50px;
    height: 30px; width: 150px;
    background: var(--green);
    color: #fff;
    font-size: 9px; font-weight: 700; letter-spacing: .06em;
    text-transform: uppercase;
    display: flex; align-items: center; justify-content: space-between;
    padding: 0 10px 0 14px;
  }
  .name-tag svg { width: 10px; height: 10px; }
  .member-role {
    margin-top: 12px;
    font-size: 8px; font-weight: 700; letter-spacing: .06em;
    color: var(--green); text-transform: uppercase;
  }

  .member-detail {
    background: var(--panel);
    border-top: 1px solid var(--line);
    height: 490px;
    padding: 40px 60px 0 60px;
    position: relative;
  }
  .detail-role {
    display: flex; align-items: center; gap: 10px;
    font-size: 8px; font-weight: 700; letter-spacing: .06em;
    color: var(--green); text-transform: uppercase;
  }
  .detail-role svg { width: 24px; height: 16px; }
  .detail-name {
    margin-top: 10px;
    font-size: 26px; font-weight: 900; letter-spacing: .02em;
    text-transform: uppercase; color: var(--ink);
  }
  .detail-rule { width: 26px; height: 2px; background: var(--green); margin: 12px 0 18px; }
  .detail-text p {
    font-size: 10.5px; line-height: 1.6; color: var(--text);
    max-width: 560px; margin-bottom: 14px;
  }
  .further-button {
    position: absolute; right: 60px; bottom: 50px;
    height: 34px; padding: 0 14px 0 18px;
    background: var(--green); color: #fff;
    font-size: 9px; font-weight: 700; letter-spacing: .08em;
    text-transform: uppercase;
    display: flex; align-items: center; gap: 18px;
  }
  .further-button svg { width: 10px; height: 10px; }

  /* ---------- mobile page ---------- */
  .mobile-page {
    position: absolute; left: 870px; top: 150px;
    width: 290px; height: 500px;
    background: var(--paper);
    overflow: hidden;
  }
  .mobile-header {
    height: 62px; padding: 0 14px;
    display: flex; align-items: center; justify-content: space-between;
    border-bottom: 1px solid var(--line);
  }
  .brand { display: flex; align-items: center; gap: 8px; }
  .brand-mark { width: 18px; height: 18px; background: var(--green); }
  .brand-name { font-size: 15px; font-weight: 700; color: var(--green); }
  .menu-toggle {
    width: 34px; height: 34px; border: 2px solid var(--green);
    display: flex; align-items: center; justify-content: center;
  }
  .menu-toggle svg { width: 14px; height: 12px; }
  .mobile-hero {
    height: 250px;
    background: linear-gradient(160deg, #6b5a4a 0%, #8a7563 40%, #2f4a42 75%, #24362f 100%);
  }
  .mobile-intro {
    position: absolute; left: 12px; right: 12px; top: 265px;
    background: var(--paper);
    padding: 16px 16px 14px;
  }
  .intro-title {
    font-size: 22px; font-weight: 400; line-height: 1.05; color: var(--ink);
  }
  .intro-title strong { color: var(--green); font-weight: 700; }
  .intro-text {
    margin-top: 10px; font-size: 9px; line-height: 1.5; color: var(--text);
  }
  .read-more {
    margin-top: 12px; text-align: right;
    font-size: 8px; font-weight: 700; color: var(--green-dark);
  }
</style>
</head>
<body>

<main class="desktop-page">
  <section class="team-row">
    <article class="member-card">
      <div class="member-photo" role="img" aria-label="Team member in dark suit and striped tie"></div>
      <div class="name-tag">Adrian Keller
        <svg viewBox="0 0 10 10"><path d="M1 5h7M5 2l3 3-3 3" stroke="#fff" stroke-width="1.4" fill="none"/></svg>
      </div>
      <p class="member-role">Project Manager</p>
    </article>
    <article class="member-card">
      <div class="member-photo" role="img" aria-label="Team member in light blue shirt with arms crossed"></div>
      <div class="name-tag">Marco Brunner
        <svg viewBox="0 0 10 10"><path d="M1 5h7M5 2l3 3-3 3" stroke="#fff" stroke-width="1.4" fill="none"/></svg>
      </div>
      <p class="member-role">Project Manager</p>
    </article>
    <article class="member-card">
      <div class="member-photo" role="img" aria-label="Team member in dark suit holding a tablet"></div>
      <div class="name-tag">Adrian Keller
        <svg viewBox="0 0 10 10"><path d="M1 5h7M5 2l3 3-3 3" stroke="#fff" stroke-width="1.4" fill="none"/></svg>
      </div>
    </article>
  </section>

  <section class="member-detail">
    <div class="detail-role">
      <svg viewBox="0 0 24 16"><path d="M6 14h13a4 4 0 0 0 0-8 6 6 0 0 0-11-1 4.5 4.5 0 0 0-2 9z" fill="none" stroke="#cfcfcf" stroke-width="1.2"/></svg>
      Project Manager
    </div>
    <h1 class="detail-name">Adrian Keller</h1>
    <div class="detail-rule"></div>
    <div class="detail-text">
      <p>My professional path began in the planning unit of a national rail operator, where I worked as a project assistant on a computer science programme. My interest in technical systems then led me to first-level support for enterprise platforms, and later to a role as system engineer. My love for project business grew at a real-time computing centre, where I supported customer projects as technical lead and later managed hosting environments for public clients.</p>
      <p>IT service management as a discipline has shaped my recent years, during which I acted as project manager in customer projects introducing service management processes.</p>
      <p>I am pleased to offer you my commitment and my broad knowledge of consulting as a Morvane consultant. More can be found on the following pages and in detail in the CV, which may be requested.</p>
    </div>
    <div class="further-button">Further
      <svg viewBox="0 0 10 10"><path d="M1 5h7M5 2l3 3-3 3" stroke="#fff" stroke-width="1.4" fill="none"/></svg>
    </div>
  </section>
</main>

<aside class="mobile-page">
  <header class="mobile-header">
    <div class="brand">
      <span class="brand-mark"></span>
      <span class="brand-name">Morvane Partners</span>
    </div>
    <div class="menu-toggle">
      <svg viewBox="0 0 14 12"><path d="M0 1h14M0 6h14M0 11h14" stroke="#6cc04a" stroke-width="2"/></svg>
    </div>
  </header>
  <div class="mobile-hero" role="img" aria-label="Smiling consultant with glasses in a green sweater, arms crossed, in an office"></div>
  <div class="mobile-intro">
    <h2 class="intro-title"><strong>Your success</strong> is<br>our motivation.</h2>
    <p class="intro-text">We think and act holistically and networked. Our consultants are structured, hands-on and focused on lasting results for your team and your business.</p>
    <p class="read-more">» Read more</p>
  </div>
</aside>

</body>
</html>
```